Speech Pathology card for parents of young children

I need a professional, yet fun card for my speech and language pathology services.
I'm trying to offer my speech therapy services to parents of young children. These parents will most likely be women. I want the card to have a fun feel to it and have a concept of speech and language in it (kind of like the cartoon I've attached below showing a boy/girl talking).

I'd want a white background on the card and to bring in some bright colors as well.

Please include the NOVRE logo in a smaller size on a free corner of the card.

Target Market(s)

parents of young children

Contact Information for Business Card

must have my information and I'd like it to have the NOVRE logo (small) somewhere in the corner)

Font styles to use
Serif
Sans Serif

Colors

Designer to choose colors to be used in the design.

Requirements
Must have
• The card title should read: Speech-Language Pathologist
• Lorena Tuvell
• MS CCC-SLP/TSSLD (this under the name)
• 555 014 2786
• lorentuvell@quillpost.net
Nice to have
• i'm looking for a card with a white background and a fun icon that encompasses speaking... similar to the one I've attached.

```html
<!DOCTYPE html>
<html lang="en">
<head>
<meta charset="utf-8">
<title>Lorena Tuvell – Speech-Language Pathologist</title>
<link href="https://fonts.googleapis.com/css2?family=Questrial&family=Roboto:wght@400;500;700&display=swap" rel="stylesheet">
<style>
  :root {
    --backdrop: #ecebe8;
    --card: #ffffff;
    --orange: #ee5a2a;
    --purple: #a3238e;
    --red: #e8432b;
    --yellow: #f0b429;
    --ink: #1a1a1a;
    --sky: #2bb3e6;
    --slate: #4a4a4a;
  }
  * { margin: 0; padding: 0; box-sizing: border-box; }
  html, body {
    width: 900px; height: 1200px; overflow: hidden;
    background: var(--backdrop);
  }
  .canvas { position: relative; width: 900px; height: 1200px; }
  .card {
    position: absolute; left: 103px; top: 385px;
    width: 695px; height: 405px;
    background: var(--card);
    border-radius: 18px;
    box-shadow: 0 4px 14px rgba(0,0,0,0.12);
  }
  .card-title {
    position: absolute; left: 44px; top: 30px;
    font-family: "Questrial", sans-serif;
    font-size: 35px; letter-spacing: 0.3px;
    white-space: nowrap;
  }
  .card-title .word-speech { color: var(--orange); }
  .card-title .word-role { color: var(--purple); }
  .speaker-illustration {
    position: absolute; left: 45px; top: 135px;
    width: 325px; height: 235px;
    border-radius: 10px;
    background: linear-gradient(120deg, #e9eaec 0%, #dff1fa 55%, #fde6d6 100%);
  }
  .contact {
    position: absolute; right: 46px; top: 138px;
    text-align: right;
    font-family: "Roboto", sans-serif;
  }
  .contact .name {
    font-family: "Questrial", sans-serif;
    font-weight: 700; font-size: 21px; color: var(--purple);
    letter-spacing: 0.5px; -webkit-text-stroke: 0.4px var(--purple);
  }
  .contact .credentials {
    margin-top: 4px; font-size: 15px; color: var(--red);
  }
  .contact-lines { margin-top: 14px; }
  .contact-line {
    display: flex; justify-content: flex-end; align-items: center;
    gap: 9px; height: 24px;
    font-size: 15px; color: var(--purple);
  }
  .contact-line .icon {
    width: 22px; height: 22px; border-radius: 50%;
    background: var(--yellow);
    display: flex; align-items: center; justify-content: center;
  }
  .association {
    position: absolute; right: 43px; top: 318px;
    display: flex; align-items: center; gap: 10px;
  }
  .association .mark {
    width: 62px; height: 62px; border-radius: 50%; background: var(--ink);
  }
  .association .name {
    font-family: "Questrial", sans-serif;
    font-size: 22px; color: var(--ink); letter-spacing: 2px;
  }
</style>
</head>
<body>
<main class="canvas">
  <section class="card">
    <h1 class="card-title"><span class="word-speech">SPEECH-LANGUAGE</span> <span class="word-role">PATHOLOGIST</span></h1>

    <div class="speaker-illustration" role="img" aria-label="Cartoon figure speaking loudly through a megaphone with colourful sound waves"></div>

    <div class="contact">
      <p class="name">LORENA TUVELL</p>
      <p class="credentials">MS CCC-SLP/TSSLD</p>
      <div class="contact-lines">
        <p class="contact-line">
          <span>555 014 2786</span>
          <span class="icon">
            <svg width="12" height="12" viewBox="0 0 24 24"><path fill="#fff" d="M6.6 10.8a15.1 15.1 0 0 0 6.6 6.6l2.2-2.2c.3-.3.7-.4 1-.2 1.1.4 2.3.6 3.6.6.6 0 1 .4 1 1V20c0 .6-.4 1-1 1A17 17 0 0 1 3 4c0-.6.4-1 1-1h3.5c.6 0 1 .4 1 1 0 1.3.2 2.5.6 3.6.1.3 0 .7-.2 1z"/></svg>
          </span>
        </p>
        <p class="contact-line">
          <span>lorentuvell@quillpost.net</span>
          <span class="icon">
            <svg width="12" height="12" viewBox="0 0 24 24"><rect x="2" y="5" width="20" height="14" rx="1.5" fill="#fff"/><path d="M3 6l9 7 9-7" fill="none" stroke="#f0b429" stroke-width="2"/></svg>
          </span>
        </p>
      </div>
    </div>

    <div class="association">
      <span class="mark"></span>
      <span class="name">NOVRE</span>
    </div>
  </section>
</main>
</body>
</html>
```